Business Card Design

A modern Thai home styled cooking . theme colors are bright orange, spring green and golden brown.I have my logo but need to be redesign coz just copied it from www. need it like it is but better.

Industry/Entity Type

Cooking

Contact Information for Business Card

Lotus Spoon by Nim(Healthier & Tastier) ,Leo Wongsakul GM, 24870 Birch ave (Rear) Glenmore MD 20477, tel 301 555 0164 , www.lotusspoonbynim.example

```html
<!DOCTYPE html>
<html lang="en">
<head>
<meta charset="utf-8">
<title>Lotus Spoon by Nim – Business Cards</title>
<link href="https://fonts.googleapis.com/css2?family=Source+Sans+3:wght@400;700&display=swap" rel="stylesheet">
<style>
  :root {
    --spring-green: #6aac43;
    --bright-orange: #e56e25;
    --footer-grey: #e6e7e8;
    --card-white: #ffffff;
    --page-bg: #ffffff;
  }
  * { margin: 0; padding: 0; box-sizing: border-box; }
  html, body {
    width: 1200px; height: 1000px; overflow: hidden;
    background: var(--page-bg);
    font-family: "Source Sans 3", "Myriad Pro", Arial, sans-serif;
  }
  .canvas { position: relative; width: 1200px; height: 1000px; }

  .card {
    position: absolute;
    width: 820px; height: 455px;
    border-radius: 24px;
    overflow: hidden;
    color: var(--card-white);
  }
  .card--green { left: 195px; top: 28px; background: var(--spring-green); --accent: var(--spring-green); }
  .card--orange { left: 187px; top: 518px; width: 818px; height: 457px; background: var(--bright-orange); --accent: var(--bright-orange); }

  .card__footer {
    position: absolute; left: 0; right: 0; top: 392px; bottom: 0;
    background: var(--footer-grey);
    display: flex; align-items: center; justify-content: center;
  }
  .card__web {
    color: var(--accent);
    font-size: 22px;
    letter-spacing: 12.5px;
    padding-left: 12px;
    margin-top: 10px;
  }

  .card__weave {
    position: absolute; left: 345px; top: 0; width: 430px; height: 392px;
  }

  .card__brand { position: absolute; left: 28px; top: 38px; width: 350px; height: 350px; }
  .card__brand-name {
    position: absolute; inset: 0;
    display: flex; align-items: center; justify-content: center;
    text-align: center;
    font-size: 40px; font-weight: 700; line-height: 1.15;
    color: var(--card-white);
  }

  .card__holder {
    position: absolute; left: 398px; top: 44px;
    font-size: 29px; font-weight: 700;
  }
  .card__company {
    position: absolute; left: 420px; width: 306px; top: 112px;
    text-align: center;
  }
  .card__company-name { font-size: 29px; line-height: 1.1; }
  .card__tagline { font-size: 21px; margin-top: 4px; }

  .card__contact {
    position: absolute; left: 430px; top: 216px;
    font-size: 29px; line-height: 43px;
  }
</style>
</head>
<body>
<main class="canvas">

  <article class="card card--green">
    <svg class="card__weave" viewBox="0 0 430 392" role="img" aria-label="Soft woven plaid stripe pattern behind the contact details">
      <defs>
        <linearGradient id="weave-green" x1="0" y1="0" x2="1" y2="1">
          <stop offset="0" stop-color="#ffffff" stop-opacity="0.14"/>
          <stop offset="1" stop-color="#ffffff" stop-opacity="0.22"/>
        </linearGradient>
      </defs>
      <rect x="0" y="85" width="428" height="218" fill="url(#weave-green)"/>
    </svg>

    <div class="card__brand">
      <svg width="350" height="350" viewBox="0 0 350 350" aria-hidden="true">
        <circle cx="175" cy="175" r="166" fill="none" stroke="#ffffff" stroke-width="6"/>
      </svg>
      <div class="card__brand-name">Lotus Spoon<br>by Nim</div>
    </div>

    <h1 class="card__holder">Leo Wongsakul GM</h1>
    <div class="card__company">
      <p class="card__company-name">Lotus Spoon by Nim</p>
      <p class="card__tagline">(Healthier &amp; Tastier)</p>
    </div>
    <address class="card__contact" style="font-style:normal">
      301-555-0164<br>
      24870 Birch ave (Rear)<br>
      Glenmore MD 20477
    </address>

    <footer class="card__footer">
      <span class="card__web">www.lotusspoonbynim.example</span>
    </footer>
  </article>

  <article class="card card--orange">
    <svg class="card__weave" viewBox="0 0 430 392" role="img" aria-label="Soft woven plaid stripe pattern behind the contact details">
      <defs>
        <linearGradient id="weave-orange" x1="0" y1="0" x2="1" y2="1">
          <stop offset="0" stop-color="#ffffff" stop-opacity="0.14"/>
          <stop offset="1" stop-color="#ffffff" stop-opacity="0.22"/>
        </linearGradient>
      </defs>
      <rect x="0" y="85" width="428" height="218" fill="url(#weave-orange)"/>
    </svg>

    <div class="card__brand">
      <svg width="350" height="350" viewBox="0 0 350 350" aria-hidden="true">
        <circle cx="175" cy="175" r="166" fill="none" stroke="#ffffff" stroke-width="6"/>
      </svg>
      <div class="card__brand-name">Lotus Spoon<br>by Nim</div>
    </div>

    <h2 class="card__holder">Leo Wongsakul GM</h2>
    <div class="card__company">
      <p class="card__company-name">Lotus Spoon by Nim</p>
      <p class="card__tagline">(Healthier &amp; Tastier)</p>
    </div>
    <address class="card__contact" style="font-style:normal">
      301-555-0164<br>
      24870 Birch ave (Rear)<br>
      Glenmore MD 20477
    </address>

    <footer class="card__footer" style="top:392px">
      <span class="card__web">www.lotusspoonbynim.example</span>
    </footer>
  </article>

</main>
</body>
</html>
```